Ledgerline Systems Group business card design.

We are a software development company that develop Software for finance companies and related industries.

We need a 2 sided business card designed. We have a new logo already designed (see attached eps and ai) We are after a clean simple corporate look. One side with just our logo, and the second side with our details.

Marcus Thelwell
Managing Director

Suite 4 Level 9, 318 Harbin Lane Sydney NSW 2000

Direct: +61 2 9478 3062
Mobile: +61 4 1237 6845
Email: marcust@lsg.net.au
Web: www.lsg.net.au

I have included 2 logo files an .ai and .eps. I noticed that the lines either side of the partners looks a bit jaggered and needs to be made sharper.

I would like to introduce a little colour somewhere rather than having it all black and white. But not over the top, keeping with a simple clean corporate look. Perhaps a light blue on some of the text?

If you have other ideas would be pleased to review

Regards

Marcus T.

```html
<!DOCTYPE html>
<html lang="en">
<head>
<meta charset="utf-8">
<title>Ledgerline Systems Group – Business Card</title>
<link href="https://fonts.googleapis.com/css2?family=Lato:wght@400;700;900&display=swap" rel="stylesheet">
<style>
  :root {
    --stage: #3a3a3a;
    --card-black: #050505;
    --brand-blue: #3d86d6;
    --ink: #1a1a1a;
    --ink-soft: #333333;
    --paper-light: #f4f4f4;
    --paper-shade: #c9c9c9;
    --stripe-light: #9a9a9a;
    --stripe-mid: #6f6f6f;
    --stripe-dark: #4a4a4a;
    --white: #ffffff;
  }
  * { margin: 0; padding: 0; box-sizing: border-box; }
  html, body {
    width: 1200px; height: 997px; overflow: hidden;
    background: var(--stage);
    font-family: "Lato", Arial, sans-serif;
  }
  .canvas { position: relative; width: 1200px; height: 997px; }

  .card {
    position: absolute; width: 600px; height: 343px;
    box-shadow: 0 18px 40px rgba(0,0,0,.55);
    overflow: hidden;
  }

  /* Brand name */
  .brand {
    display: flex; align-items: center; gap: 12px;
    color: var(--brand-blue); font-weight: 900;
    text-transform: uppercase; letter-spacing: 1px; white-space: nowrap;
  }
  .brand-mark { width: 14px; height: 14px; background: var(--brand-blue); flex: none; }

  /* Front */
  .card-front { left: 80px; top: 100px; background: var(--card-black); }
  .card-front .brand {
    position: absolute; left: 0; right: 0; top: 152px;
    justify-content: center; font-size: 28px;
  }

  /* Back */
  .card-back {
    left: 520px; top: 540px;
    background: linear-gradient(90deg, var(--paper-shade) 0%, var(--paper-light) 45%, var(--paper-light) 70%, var(--paper-shade) 100%);
  }
  .back-header {
    position: absolute; left: 0; top: 0; width: 100%; height: 142px;
    background: var(--card-black);
  }
  .card-back .brand {
    position: absolute; left: 0; right: 0; top: 86px;
    justify-content: center; font-size: 21px;
  }
  .header-stripes { position: absolute; left: 0; top: 142px; width: 100%; }
  .header-stripes span { display: block; height: 3px; margin-bottom: 3px; background: var(--stripe-light); }
  .header-stripes span:nth-child(2) { background: var(--stripe-mid); }
  .header-stripes span:nth-child(3) { background: var(--stripe-dark); }

  .holder { position: absolute; left: 70px; top: 248px; color: var(--ink); }
  .holder-name { font-size: 23px; font-weight: 900; letter-spacing: .5px; text-transform: uppercase; }
  .holder-title { font-size: 15px; font-weight: 700; text-transform: uppercase; color: var(--ink-soft); margin-top: 2px; }

  .contact { position: absolute; left: 345px; top: 170px; color: var(--ink); }
  .contact-address { font-size: 14px; font-weight: 900; line-height: 18px; margin-bottom: 8px; white-space: nowrap; }
  .contact-row { display: flex; align-items: center; gap: 9px; height: 22px; margin-bottom: 5px; font-size: 13px; white-space: nowrap; }
  .contact-icon {
    width: 22px; height: 22px; background: var(--ink); flex: none;
    display: flex; align-items: center; justify-content: center;
  }
  .contact-web { font-size: 16px; font-weight: 900; margin-top: 3px; }
</style>
</head>
<body>
<main class="canvas">

  <section class="card card-front" aria-label="Card front">
    <div class="brand"><span class="brand-mark"></span>Ledgerline Systems Group</div>
  </section>

  <section class="card card-back" aria-label="Card back">
    <div class="back-header">
      <div class="brand"><span class="brand-mark"></span>Ledgerline Systems Group</div>
    </div>
    <div class="header-stripes"><span></span><span></span><span></span></div>

    <div class="holder">
      <div class="holder-name">Marcus Thelwell</div>
      <div class="holder-title">Managing Director</div>
    </div>

    <div class="contact">
      <div class="contact-address">
        <div>Suite 4 Level 9, 318,</div>
        <div>Harbin Lane Sydney NSW 2000</div>
      </div>
      <div class="contact-row">
        <span class="contact-icon">
          <svg width="14" height="14" viewBox="0 0 24 24"><path fill="#fff" d="M6.6 10.8a15 15 0 0 0 6.6 6.6l2.2-2.2c.3-.3.7-.4 1-.2 1.1.4 2.3.6 3.6.6.6 0 1 .4 1 1V20c0 .6-.4 1-1 1A17 17 0 0 1 3 4c0-.6.4-1 1-1h3.5c.6 0 1 .4 1 1 0 1.3.2 2.5.6 3.6.1.3 0 .7-.2 1z"/></svg>
        </span>+61 2 9478 3062
      </div>
      <div class="contact-row">
        <span class="contact-icon">
          <svg width="14" height="14" viewBox="0 0 24 24"><rect x="6" y="2" width="12" height="20" rx="2" fill="none" stroke="#fff" stroke-width="2"/><circle cx="12" cy="18" r="1.2" fill="#fff"/></svg>
        </span>+61 4 1237 6845
      </div>
      <div class="contact-row">
        <span class="contact-icon">
          <svg width="14" height="14" viewBox="0 0 24 24"><rect x="2" y="5" width="20" height="14" fill="none" stroke="#fff" stroke-width="2"/><path d="M2 5l10 8 10-8" fill="none" stroke="#fff" stroke-width="2"/></svg>
        </span>marcust@lsg.net.au
      </div>
      <div class="contact-web">www.lsg.net.au</div>
    </div>
  </section>

</main>
</body>
</html>
```